Branding for salad and dip containers - retail

we are trying to modernise our packaging design
the lids will be pre-printed (only with our logo) the design can be any shape, preferably not covering the whole top as we want the product to show
NO OTHER details are needed on the lid! Just the logo in bold modern design (using our existing logo and colours) fresh modern and bold
this is the container size we use
https://www.pakbrook.co.uk/acatalog/280ml-rectangular-clear-tamperproof-container-lid.html#SID=64
see images attached of some trials made that we don’t like
1) One has too many other details
2) The other has not utilised our brand and logo

Target Market(s)

Retail Customers

Industry/Entity Type

food

Requirements
Must have
• our current existing logo included
Nice to have
• i would like to see my logo rebranded in a modern sleek design ready to printed on container tops
Should not have
• none of the current add ons- just logo bold and modern

```html
<!DOCTYPE html>
<html lang="en">
<head>
<meta charset="utf-8">
<title>Fernley's lid label</title>
<link rel="stylesheet" href="https://fonts.googleapis.com/css2?family=Roboto+Slab:wght@500&display=swap">
<style>
  :root {
    --canvas-bg: #f3f3f3;
    --brand-red: #d5323a;
    --pattern-red: #dc4249;
    --edge-dark: #333333;
    --badge-white: #ffffff;
    --wordmark: #ffffff;
  }
  html, body {
    margin: 0;
    padding: 0;
    overflow: hidden;
  }
  .canvas {
    position: relative;
    width: 853px;
    height: 1200px;
    background: var(--canvas-bg);
    overflow: hidden;
  }
  .lid-label {
    position: absolute;
    inset: 0;
    width: 853px;
    height: 1200px;
  }
  .label-band { fill: var(--brand-red); }
  .label-edge { fill: var(--edge-dark); }
  .brand-badge {
    fill: var(--badge-white);
    filter: drop-shadow(0 3px 4px rgba(0,0,0,0.18));
  }
  .wordmark {
    font-family: "Roboto Slab", Georgia, serif;
    font-weight: 500;
    font-size: 96px;
    fill: var(--wordmark);
  }
</style>
</head>
<body>
  <main class="canvas">
    <svg class="lid-label" viewBox="0 0 853 1200" xmlns="http://www.w3.org/2000/svg">
      <defs>
        <clipPath id="band-clip">
          <path d="M437,226 H645 Q662,226 662,243 V963 Q662,980 645,980 H458 C400,940 338,880 340,790 C344,700 420,640 448,540 C465,470 445,300 437,226 Z"/>
        </clipPath>
        <radialGradient id="leaf-tone" cx="0.5" cy="0.5" r="0.5">
          <stop offset="0" stop-color="var(--pattern-red)" stop-opacity="1"/>
          <stop offset="1" stop-color="var(--pattern-red)" stop-opacity="0"/>
        </radialGradient>
      </defs>

      <path class="label-edge"
            d="M430,226 H645 Q662,226 662,243 V963 Q662,980 645,980 H446 C388,940 324,880 326,790 C330,700 406,640 434,540 C451,470 432,300 430,226 Z"/>
      <path class="label-band"
            d="M437,226 H645 Q662,226 662,243 V963 Q662,980 645,980 H458 C400,940 338,880 340,790 C344,700 420,640 448,540 C465,470 445,300 437,226 Z"/>

      <g clip-path="url(#band-clip)">
        <ellipse cx="465" cy="825" rx="110" ry="160" fill="url(#leaf-tone)"
                 role="img" aria-label="Scattered outline leaf pattern"/>
      </g>

      <circle class="brand-badge" cx="411" cy="411" r="138"/>

      <text class="wordmark" transform="translate(647,950) rotate(-90)"
            x="0" y="0" textLength="456" lengthAdjust="spacingAndGlyphs">Fernley’s</text>
    </svg>
  </main>
</body>
</html>
```